Birch Tidy Yard Frost Maintenance

I need a logo with a roughly horizontal rectangular shape incorporating the color green and white. I want the green part to have the word green and white letters and the clean part to have the word clean in green letters
Updates

Would really appreciate a graphic grass image along bottom of design Added Wednesday, April 22, 2015

Target Market(s)

Baby Boomers who want to remain in their homes

Contact Information for Business Card

back of card will list the following details vertically;Phrase 1
Affordable Reliable Trustworthy, Phrase 2 Give yourself Freedom and Peace-of-Mind Phrase 3 Commercial Grade Equipment Phrase 4 Each Lawn neatly Cut, Trimmed and Air Blown for that Professional Touch!

Font styles to use
Other font styles liked:
• Calibri preferred

Requirements
Must have
• The word ESTIMATE and a line at bottom, back of card for easy fill in
Nice to have
• Beautiful Grass detail along bottom front of card

```html
<!DOCTYPE html>
<html lang="en">
<head>
<meta charset="utf-8">
<title>Birch Tidy Yard Frost Maintenance – Business Card</title>
<link href="https://fonts.googleapis.com/css2?family=Carlito:wght@400;700&display=swap" rel="stylesheet">
<style>
  :root {
    --canvas: #d9dbdc;
    --card: #f7f7f5;
    --green: #8cc63f;
    --green-soft: #c5e19a;
    --ink: #1e1e1e;
    --ink-soft: #333;
    --rule: #9aa0a4;
    --card-shadow: 0 18px 40px rgba(0,0,0,0.18), 0 2px 6px rgba(0,0,0,0.12);
  }
  * { box-sizing: border-box; margin: 0; padding: 0; }
  html, body {
    width: 1200px; height: 1200px; overflow: hidden;
    background: var(--canvas);
    font-family: "Carlito", "Calibri", sans-serif;
    color: var(--ink);
  }
  .sheet {
    width: 1200px; height: 1200px;
    display: flex; flex-direction: column; align-items: center;
    justify-content: center; gap: 60px;
  }
  .card {
    position: relative;
    width: 840px; height: 480px;
    background: var(--card);
    box-shadow: var(--card-shadow);
    overflow: hidden;
  }

  /* Contact side */
  .holder { position: absolute; left: 56px; top: 50px; }
  .holder__name { font-weight: 700; font-size: 30px; letter-spacing: 0.5px; }
  .holder__title { font-size: 24px; color: var(--ink-soft); margin-top: 2px; }

  .divider {
    position: absolute; left: 56px; top: 182px;
    width: 440px; height: 6px;
    background: linear-gradient(90deg, rgba(140,198,63,0) 0%, var(--green) 35%, var(--green) 100%);
  }

  .contacts {
    position: absolute; left: 56px; top: 212px;
    list-style: none; font-size: 25px; line-height: 1.15; color: var(--ink-soft);
  }
  .contacts li { display: flex; align-items: flex-start; gap: 12px; margin-bottom: 4px; }
  .contacts svg { flex: 0 0 22px; width: 22px; height: 22px; margin-top: 3px; }

  .wordmark {
    font-weight: 700; color: var(--green);
    display: flex; align-items: center; gap: 12px;
    line-height: 1;
  }
  .wordmark__dot { background: var(--green); border-radius: 50%; flex: none; }
  .wordmark__text { display: flex; flex-direction: column; }

  .card--contact .wordmark {
    position: absolute; right: 48px; top: 150px; font-size: 40px;
  }
  .card--contact .wordmark__dot { width: 34px; height: 34px; }
  .card--contact .wordmark__sub { font-size: 22px; margin-top: 6px; }

  .swoosh { position: absolute; right: 0; bottom: 0; width: 840px; height: 160px; }

  /* Brand side */
  .card--brand {
    display: flex; flex-direction: column; align-items: center;
    justify-content: space-between;
    padding: 48px 56px 40px;
  }
  .card--brand .wordmark { font-size: 64px; gap: 20px; }
  .card--brand .wordmark__dot { width: 52px; height: 52px; }
  .card--brand .wordmark__sub { font-size: 34px; margin-top: 8px; }

  .promises {
    list-style: none; text-align: center;
    font-size: 21px; line-height: 1.4; color: var(--ink-soft);
  }
  .promises li::before {
    content: ""; display: inline-block; width: 8px; height: 8px;
    border-radius: 50%; background: var(--green);
    margin-right: 10px; vertical-align: middle;
  }

  .estimate {
    width: 100%;
    display: flex; align-items: flex-end; gap: 16px;
  }
  .estimate__label {
    font-weight: 700; font-size: 26px; letter-spacing: 2px; color: var(--green);
    line-height: 1;
  }
  .estimate__line { flex: 1; border-bottom: 2px solid var(--rule); height: 0; margin-bottom: 3px; }
</style>
</head>
<body>
<main class="sheet">

  <section class="card card--contact" aria-label="Business card, contact side">
    <div class="holder">
      <p class="holder__name">YOUR FULL NAME</p>
      <p class="holder__title">Your title</p>
    </div>

    <div class="divider"></div>

    <ul class="contacts">
      <li>
        <svg viewBox="0 0 22 22" aria-hidden="true"><circle cx="11" cy="11" r="11" fill="var(--green)"/><path d="M7 6.5c0 5 3.5 9 8.5 9l1-2.2-2.4-1.2-1.1 1.2c-1.6-.7-2.9-2-3.6-3.6l1.2-1.1L9.4 6.2z" fill="#fff"/></svg>
        <span>012-345-6789</span>
      </li>
      <li>
        <svg viewBox="0 0 22 22" aria-hidden="true"><circle cx="11" cy="11" r="11" fill="var(--green)"/><rect x="7.5" y="5" width="7" height="12" rx="1.3" fill="#fff"/><rect x="8.8" y="6.6" width="4.4" height="7.5" fill="var(--green)"/></svg>
        <span>012-345-6789</span>
      </li>
      <li>
        <svg viewBox="0 0 22 22" aria-hidden="true"><circle cx="11" cy="11" r="11" fill="var(--green)"/><rect x="5.5" y="7" width="11" height="8" rx="1" fill="#fff"/><path d="M5.8 7.4 11 11.6l5.2-4.2" stroke="var(--green)" stroke-width="1.3" fill="none"/></svg>
        <span>your email adress</span>
      </li>
      <li>
        <svg viewBox="0 0 22 22" aria-hidden="true"><circle cx="11" cy="11" r="11" fill="var(--green)"/><path d="M11 4.5a4.3 4.3 0 0 0-4.3 4.3c0 3.2 4.3 8.2 4.3 8.2s4.3-5 4.3-8.2A4.3 4.3 0 0 0 11 4.5z" fill="#fff"/><circle cx="11" cy="8.8" r="1.6" fill="var(--green)"/></svg>
        <span>Your company address line 1<br>City zipcode line 2</span>
      </li>
    </ul>

    <div class="wordmark">
      <span class="wordmark__dot" aria-hidden="true"></span>
      <span class="wordmark__text">
        <span>Birch Tidy</span>
        <span class="wordmark__sub">Yard Frost Maintenance</span>
      </span>
    </div>

    <svg class="swoosh" viewBox="0 0 840 160" preserveAspectRatio="none" aria-hidden="true">
      <path d="M380 160 C 560 130, 720 95, 840 70 L 840 160 Z" fill="var(--green)"/>
      <path d="M300 160 C 520 120, 700 80, 840 55 L 840 72 C 700 98, 540 132, 390 160 Z" fill="var(--green-soft)"/>
    </svg>
  </section>

  <section class="card card--brand" aria-label="Business card, brand side">
    <div class="wordmark">
      <span class="wordmark__dot" aria-hidden="true"></span>
      <span class="wordmark__text">
        <span>Birch Tidy</span>
        <span class="wordmark__sub">Yard Frost Maintenance</span>
      </span>
    </div>

    <ul class="promises">
      <li>Affordable Reliable Trustworthy</li>
      <li>Give yourself Freedom and Peace-of-Mind</li>
      <li>Commercial Grade Equipment</li>
      <li>Each Lawn neatly Cut, Trimmed and Air Blown for that Professional Touch!</li>
    </ul>

    <div class="estimate">
      <span class="estimate__label">ESTIMATE</span>
      <span class="estimate__line" aria-hidden="true"></span>
    </div>
  </section>

</main>
</body>
</html>
```